Children's book business card contest - The more bright colors the better

Hello

PLEASE incorporate THE CHARACTERS ILLUSTRATIONS on the most recent uploaded attachment on the business card.

I'm in the process of completing my first manuscript for my children's book series BiBi SPINS a series of stories from a blended family.

My illustrator and I just completed our logo which you will find attached. Additionally you will find my first idea for my business card which I took from Cardwellex just says it means to get started but I really like the color schema. I will be getting my business card out to editors, agents, teachers, and anyone in the children's book realm. The card needs to be bright, friendly and inviting. It needs to remind you of children I do want a double sided card but I am very open as far as design layout. Below is a description of the book series and how the series will go to give you motivation or ideas. Please only submit injuries worthy of national recognition as the business cards will be passed out across the country to some of the top writing professionals in the industry at a childrens writing conference I will be attending.

Like I mentioned previously please review the information below as it gives you background too much children's book series. I look forward to working with my designer and I look forward to the submissions.

"I'm looking for someone with experience in illustrating children's books and is also passionate about this specific illustration type. My book series will be a series of short stories from a blended family. Each book well always have the same characters but the storyline will be different. Additionally, I'm looking for someone who has experience in taking real life photos and creating real like cartoon illustrations. My children's book series idea is based off of my family and I want us to be the characters. Also, if you have a writing background and could help me with editing that would be a very big plus as well. One of the niches for my children's book series is that my blended family is also blended because of ethnicity. My children's book series will bring light to multiculturalism in families and the different diversities blended families go through. This is an untapped industry in the children's book market. If you have experience with grant writing I am very interested in that as well. Please feel free to respond to any of my needs that you feel you are applicable for. I know I've created an idea that will revolutionize how parents and children read and learn together. My book series idea is innovative, fun and has tremendous crossover ability. Please only reply if you are seriously interested and have current availability. I'm ready to be GREAT and I hope you don't pass on the opportunity to join me! "

Please note: I will be using Cardwellex for my business card ordering so please constructive business card to fit those parameters. Additionally there are three attachments I provided one of them is the actual logo, the other is the almost completed book cover, and the other one is my current business cards from Cardwellex that I am looking to replace.

Target Market(s)

Children and Writing Professionals

Industry/Entity Type

Business

Contact Information for Business Card

I would like this business card to be very colorful. The card needs to attract business writing professionals as well as appeal to children and teachers inside the schooling network

Font styles to use
Serif
Sans Serif

Requirements
Must have
• A lot of color, characteristic, informative and must have all of my contact information
Nice to have
• Originality

```html
<!DOCTYPE html>
<html lang="en">
<head>
<meta charset="utf-8">
<title>BiBi SPINS – Business Card</title>
<link rel="stylesheet" href="https://fonts.googleapis.com/css2?family=Delius&display=swap">
<style>
  :root {
    --backdrop: #d9d9d9;
    --card-white: #f1f1f0;
    --red: #ee0d12;
    --red-deep: #e5141c;
    --pink: #f58a8f;
    --pink-soft: #f5a5a6;
    --white: #ffffff;
    --art-top: #4a5aa8;
    --art-bottom: #9a6a3e;
  }
  html, body {
    margin: 0;
    width: 1200px;
    height: 836px;
    overflow: hidden;
    background: var(--backdrop);
  }
  .business-card {
    position: absolute;
    left: 50px;
    top: 104px;
    width: 1100px;
    height: 628px;
    box-shadow: 0 10px 30px rgba(0,0,0,0.18);
  }
  .card-text { font-family: "Delius", "Comic Sans MS", sans-serif; fill: var(--white); }
  .owner-name { font-size: 58px; }
  .owner-role { font-size: 32px; }
  .series-name { font-size: 52px; fill: var(--red); }
  .contact-line { font-size: 22px; }
  .contact-phone { font-size: 38px; }
  .tagline { font-size: 24px; }
  .icon { fill: none; stroke: var(--white); stroke-width: 2.4; }
  .highlight { fill: none; stroke: var(--white); stroke-linecap: round; }
</style>
</head>
<body>
<svg class="business-card" viewBox="0 0 1100 628" xmlns="http://www.w3.org/2000/svg">
  <defs>
    <linearGradient id="family-art-tone" x1="0" y1="0" x2="0" y2="1">
      <stop offset="0" stop-color="var(--art-top)"/>
      <stop offset="0.7" stop-color="#6d80b8"/>
      <stop offset="1" stop-color="var(--art-bottom)"/>
    </linearGradient>
    <clipPath id="card-shape"><rect width="1100" height="628"/></clipPath>
  </defs>

  <g clip-path="url(#card-shape)">
    <rect class="card-base" width="1100" height="628" fill="var(--card-white)"/>

    <rect class="family-illustration" role="img" aria-label="Illustration of the blended family: father, mother, son and their dog"
          x="70" y="80" width="260" height="460" rx="40" fill="url(#family-art-tone)" opacity="0.85"/>

    <path class="blob-top" d="M560 0 H1100 V330 C1000 300 900 250 760 250 C660 250 600 200 575 130 C560 90 555 40 560 0 Z" fill="var(--red)"/>

    <path class="blob-bottom" d="M300 628 C370 540 480 490 620 480 C760 470 900 500 1100 470 V628 Z" fill="var(--red-deep)"/>
    <path class="highlight" d="M525 530 C565 512 615 503 660 502" stroke-width="7"/>

    <path class="blob-series" d="M380 230 C420 170 560 160 650 190 C720 215 730 300 710 370 C690 440 580 470 480 460 C390 450 340 390 350 320 C355 280 365 250 380 230 Z"
          fill="var(--pink-soft)" stroke="var(--pink)" stroke-width="10"/>
    <path class="highlight" d="M470 200 C520 190 580 190 620 200" stroke-width="7"/>

    <path class="blob-contact" d="M720 300 C790 255 1000 250 1100 290 V510 C1000 545 850 545 770 510 C690 470 670 340 720 300 Z"
          fill="var(--pink)" stroke="var(--red)" stroke-width="8"/>
    <path class="highlight" d="M765 298 C805 286 850 282 890 284" stroke-width="6"/>

    <text class="card-text owner-name" x="1060" y="105" text-anchor="end">Marisol Bennett</text>
    <text class="card-text owner-role" x="1060" y="150" text-anchor="end">Author/Founder</text>

    <text class="card-text series-name" x="520" y="335" text-anchor="middle">BiBi SPINS</text>

    <g class="contact-details">
      <rect class="icon" x="790" y="316" width="24" height="17" rx="2"/>
      <path class="icon" d="M790 318 L802 327 L814 318"/>
      <text class="card-text contact-line" x="828" y="332">marisol@bibispins.xyz</text>

      <rect class="icon" x="794" y="352" width="16" height="28" rx="3"/>
      <text class="card-text contact-phone" x="828" y="380">555.210.4478</text>

      <circle cx="802" cy="407" r="9" fill="var(--white)"/>
      <text class="card-text contact-line" x="828" y="414">Follow me on Chirper</text>
      <text class="card-text contact-line" x="828" y="442">@bibi_spins_xyz</text>

      <circle class="icon" cx="802" cy="472" r="11"/>
      <ellipse class="icon" cx="802" cy="472" rx="5" ry="11"/>
      <path class="icon" d="M791 472 H813"/>
      <text class="card-text contact-line" x="828" y="480">www.bibispins.xyz</text>
    </g>

    <text class="card-text tagline" x="720" y="592" text-anchor="middle">A series of short stories from a blended family</text>
  </g>
</svg>
</body>
</html>
```